依頼詳細
❏依頼内容

「リッチメッセージ」1点と「リッチメニュー」1点
をお願いします。高級感があり、可愛らしさも入れたデザインでお願いしたいです。

挨拶メッセージで2つの画像を合わせると一つの画像になるような
ブランディングを狙ったリッチメニュー+リッチメッセージ
にしたいです。

❏概要
◯サ−ビス
物販、集客が苦手なエステ、ネイル、美容室などのサロン経営者に向けたコンサルタント。
◯タ−ゲット
おひとりサロン、スタッフ4人までのサロン経営者。
お店の物販、リピーターに困ってる経営者。
30代〜50代くらい

◯講師人物像
見た目はキリッとしているが、話上手で話しやすい方。
こだわりをしっかりと持ち、任せても良いと信頼できる方。

❏デザイン依頼
・使用して欲しい色;マゼンタピンク
・可愛く、カッコよく、高級感を入れて

❏依頼詳細
<作成物>
■リッチメッセージ
リッチメニュー
合計2枚

〈リッチメニューの項目〉
上の段左から右へ①〜③
下の段左から右へ④〜⑥

〈リッチメニューの表示名〉
①自己紹介   ②売れる物販セミナー   ③SNS
④お悩み診断 ⑤お友達紹介 ⑥オンラインショップ

デザイン重視でここの表示名はデザイン的に英語の方がよければ
英語でも大丈夫です。

〈画像はこちらから〉
↓ソラボックスリンク
https://3.kumobako-share.example/0417-a93f1e7b0d52c8aa4e61f7d3b90c2e58

※こちらの作成以外に勝手に使用された場合は
著作権侵害で法的手段をとらせていただきます。
作成事例にも使用しないでください。

<サイズ>
・リッチメッセージ(1040×1040ピクセル)
・リッチメニュー(1200×810ピクセル)

<納品形式>
・ai形式(イラストレーターデータ)
・JPG
<詳細>
※添付ファイルをご確認ください。

<備考>
納品前の修正について、回数制限などありますか?
納品後の修正について、回数制限や料金などを教えて下さい。
色々なデザインでのご応募をお待ちしております!
記載項目
サイズ
• ・リッチメッセージ(1040×1040ピクセル) ・リッチメニュー(1200×810ピクセル)
希望イメージ
シンプル 複雑
単色 カラフル
暗い 明るい
日常 高級
遊び心 厳粛
未来的 伝統的
女性的 男性的
希望する色
赤系、マゼンタピンク
納品ファイル
• 高解像度JPG (.jpg)
• イラストレーター形式 (.ai)
補足説明

```html
<!DOCTYPE html>
<html lang="ja">
<head>
<meta charset="utf-8">
<title>Salon Consulting リッチメニュー</title>
<link href="https://fonts.googleapis.com/css2?family=Noto+Serif+JP:wght@500;700&family=Great+Vibes&family=Cormorant+Garamond:wght@500&display=swap" rel="stylesheet">
<style>
  :root {
    --magenta: #d6177a;
    --magenta-deep: #b80f63;
    --magenta-soft: #e8479a;
    --gold: #c9a75a;
    --white: #ffffff;
    --paper: #f6f4f3;
    --tile-line: rgba(255,255,255,0.75);
    --tile-fill: rgba(255,255,255,0.10);
  }
  * { margin: 0; padding: 0; box-sizing: border-box; }
  html, body { width: 803px; height: 1200px; overflow: hidden; background: var(--white); }
  .menu {
    position: relative; width: 803px; height: 1200px; overflow: hidden;
    font-family: "Noto Serif JP", serif;
  }
  .hero-photo {
    position: absolute; left: 0; top: 0; width: 803px; height: 640px;
    background: linear-gradient(100deg, var(--paper) 0%, #ece9e8 55%, #dcd6d4 100%);
  }
  .flower-cluster {
    position: absolute; border-radius: 50%;
    background: radial-gradient(circle, #f3d6d8 0%, #e6ccb8 55%, rgba(230,220,200,0) 75%);
  }
  .flower-top { left: 300px; top: 40px; width: 190px; height: 140px; }
  .flower-bottom { left: 110px; top: 320px; width: 210px; height: 220px; }
  .frame { position: absolute; left: 0; top: 0; }
  .hero-copy {
    position: absolute; text-align: center;
  }
  .hero-tag {
    left: 168px; width: 314px; top: 238px; height: 42px; line-height: 42px;
    background: var(--magenta); color: var(--white);
    font-size: 23px; font-weight: 500; letter-spacing: 0.04em;
  }
  .hero-lead {
    left: 140px; width: 370px; top: 292px; color: var(--magenta);
    font-size: 22px; font-weight: 700; line-height: 1.55; letter-spacing: 0.03em;
  }
  .wave { position: absolute; left: 0; top: 540px; }
  .brand-script {
    position: absolute; left: 420px; top: 596px;
    font-family: "Great Vibes", cursive; font-size: 36px; color: var(--white);
  }
  .rose-field {
    position: absolute; left: 0; top: 660px; width: 803px; height: 540px;
    background: radial-gradient(ellipse at 30% 60%, var(--magenta-soft) 0%, var(--magenta) 45%, var(--magenta-deep) 100%);
  }
  .tile {
    position: absolute; width: 230px; height: 228px;
    border: 2px solid var(--tile-line); background: var(--tile-fill);
    color: var(--white); text-align: center;
  }
  .tile svg { position: absolute; left: 80px; top: 38px; width: 70px; height: 70px; }
  .tile-label {
    position: absolute; left: 0; right: 0; top: 128px;
    font-size: 23px; font-weight: 700; letter-spacing: 0.02em; white-space: nowrap;
  }
  .tile-label.small { font-size: 21px; }
  .tile-sub {
    position: absolute; left: 0; right: 0; top: 164px;
    font-family: "Cormorant Garamond", serif; font-size: 18px; line-height: 1.1;
  }
  .c1 { left: 32px; } .c2 { left: 294px; } .c3 { left: 546px; }
  .r1 { top: 672px; } .r2 { top: 926px; }
</style>
</head>
<body>
<main class="menu">
  <div class="hero-photo" role="img" aria-label="白い室内で微笑む講師の写真"></div>
  <div class="flower-cluster flower-top" role="img" aria-label="ピンクと白の花のアレンジメント"></div>
  <div class="flower-cluster flower-bottom" role="img" aria-label="ピンクと白の花と葉のアレンジメント"></div>

  <svg class="frame" width="803" height="640" viewBox="0 0 803 640" aria-hidden="true">
    <polygon points="325,62 510,165 510,345 325,448 140,345 140,165" fill="rgba(255,255,255,0.85)" stroke="var(--gold)" stroke-width="2.5"/>
    <polygon points="325,76 497,172 497,338 325,434 153,338 153,172" fill="none" stroke="var(--gold)" stroke-width="1"/>
  </svg>

  <p class="hero-copy hero-tag">エステ・ネイル・美容室</p>
  <p class="hero-copy hero-lead">物販、集客を改善し<br>あなたのサロン経営を<br>安定させませんか？</p>

  <svg class="wave" width="803" height="130" viewBox="0 0 803 130" aria-hidden="true">
    <path d="M0,70 C180,40 330,115 520,80 C650,56 740,40 803,30 L803,130 L0,130 Z" fill="var(--magenta)"/>
    <path d="M0,62 C180,32 330,107 520,72 C650,48 740,32 803,22" fill="none" stroke="var(--magenta-soft)" stroke-width="3"/>
  </svg>
  <p class="brand-script">Salon Consulting</p>

  <div class="rose-field" role="img" aria-label="マゼンタピンクのバラの背景"></div>

  <a class="tile c1 r1">
    <svg viewBox="0 0 70 70" fill="var(--white)"><path d="M35 8 L40 30 L62 35 L40 40 L35 62 L30 40 L8 35 L30 30Z"/><path d="M56 6 L58 13 L65 15 L58 17 L56 24 L54 17 L47 15 L54 13Z"/></svg>
    <p class="tile-label">自己紹介</p>
    <p class="tile-sub">About us</p>
  </a>
  <a class="tile c2 r1">
    <svg viewBox="0 0 70 70" fill="var(--white)"><path d="M35 62 C10 44 6 32 10 24 C15 14 29 14 35 26 C41 14 55 14 60 24 C64 32 60 44 35 62Z"/><path d="M56 6 C52 3 48 6 50 10 L56 16 L62 10 C64 6 60 3 56 6Z"/></svg>
    <p class="tile-label small">売れる物販セミナー</p>
    <p class="tile-sub">Product sales<br>Seminar</p>
  </a>
  <a class="tile c3 r1">
    <svg viewBox="0 0 70 70" fill="none" stroke="var(--white)" stroke-width="3.5"><rect x="14" y="6" width="42" height="58" rx="6"/><circle cx="33" cy="30" r="9"/><line x1="40" y1="37" x2="47" y2="44"/></svg>
    <p class="tile-label">SNS</p>
    <p class="tile-sub">Social media</p>
  </a>
  <a class="tile c1 r2">
    <svg viewBox="0 0 70 70" fill="none" stroke="var(--white)" stroke-width="3.5"><rect x="13" y="10" width="44" height="54" rx="4"/><rect x="25" y="5" width="20" height="9" rx="2" fill="var(--white)"/><path d="M21 27 l4 4 7-7 M21 42 l4 4 7-7"/><line x1="37" y1="29" x2="49" y2="29"/><line x1="37" y1="44" x2="49" y2="44"/></svg>
    <p class="tile-label">お悩み診断</p>
    <p class="tile-sub">Trouble diagnosis</p>
  </a>
  <a class="tile c2 r2">
    <svg viewBox="0 0 70 70" fill="var(--white)"><circle cx="22" cy="22" r="10"/><circle cx="48" cy="22" r="10"/><path d="M4 58 C4 42 14 36 22 36 C30 36 40 42 40 58Z"/><path d="M30 58 C30 42 40 36 48 36 C56 36 66 42 66 58Z"/></svg>
    <p class="tile-label">お友達紹介</p>
    <p class="tile-sub">Introducing friends</p>
  </a>
  <a class="tile c3 r2">
    <svg viewBox="0 0 70 70" fill="none" stroke="var(--white)" stroke-width="3.5"><path d="M12 24 H58 L54 64 H16Z" fill="var(--white)"/><path d="M25 26 V18 C25 8 45 8 45 18 V26"/></svg>
    <p class="tile-label small">オンラインショップ</p>
    <p class="tile-sub">Online Shop</p>
  </a>
</main>
</body>
</html>
```